Occupational Therapist does home accessibility for disabled folks; needs business card design

We need a business card for a company in Portland, Oregon that specializes in making homes accessible, comfortable, and functional for people who are disabled or aging who would like to stay in THEIR home. Our medical background as Occupational Therapists allows us to translate the functional needs of the person into the recommendations for the design of the home remodel.

Target Market(s)

Elderly, children of elderly
People with disabilities, families of people with disabilities

Industry/Entity Type

Business

Contact Information for Business Card

Company name: HomeWise
Name: Danielle Reyes Crawford, OTR/L, CAPS, ECHM
Occupational Therapist, Home Modification & Accessibility Specialist
website: www.homewiseforyears.com
email: homewiseforyears@nestmail.example
phone: (503)218-4057
CCB #: 487315

Font styles to use
Sans Serif

Requirements
Must have
• My logo
• Easy to read font with contrasting background
• Please list the Services offered: Occupational Therapy, Home safety & accessibility assessments, Home modification consulting, project management
Nice to have
• Friendly, welcoming feel
Should not have
• Dark colored background

```html
<!DOCTYPE html>
<html lang="en">
<head>
<meta charset="utf-8">
<title>HomeWise business card</title>
<link rel="stylesheet" href="https://fonts.googleapis.com/css2?family=Jost:wght@400;500;600&display=swap">
<style>
  :root{
    --orange:#d0822a;
    --grey:#6a6a6a;
    --grey-dark:#5b5b5b;
    --white:#ffffff;
    --page:#ecebe8;
  }
  *{margin:0;padding:0;box-sizing:border-box}
  html,body{width:1200px;height:900px;overflow:hidden;background:var(--page)}
  body{font-family:"Jost",sans-serif;position:relative}
  .card{position:absolute;width:660px;height:377px;overflow:hidden;box-shadow:0 6px 18px rgba(0,0,0,.18)}
  .card-front{left:270px;top:50px;background:var(--orange);color:var(--white)}
  .card-back{left:270px;top:473px;background:var(--orange)}

  /* front */
  .brand-front{position:absolute;left:62px;top:118px;display:flex;align-items:center;gap:14px}
  .brand-mark{width:22px;height:22px;background:var(--white)}
  .brand-name{font-size:58px;font-weight:500;letter-spacing:.5px;line-height:1}
  .services{position:absolute;left:62px;top:236px;font-size:17px;letter-spacing:1.4px;line-height:1.35;font-weight:400}
  .services .dot{display:inline-block;width:6px;height:6px;background:var(--grey);border-radius:50%;vertical-align:middle;margin:0 5px}
  .site-front{position:absolute;left:62px;top:306px;font-size:17px;letter-spacing:.5px}
  .site-front b{font-weight:600}

  /* back */
  .swoop{position:absolute;inset:0}
  .brand-back{position:absolute;right:40px;top:48px;display:flex;align-items:center;gap:12px;color:var(--orange)}
  .brand-back .brand-mark{background:var(--orange);width:18px;height:18px}
  .brand-back .brand-name{font-size:46px}
  .details{position:absolute;right:40px;top:128px;text-align:right;color:var(--grey-dark)}
  .person{font-size:20px;font-weight:600;color:var(--orange);letter-spacing:.5px}
  .role{font-size:14px;line-height:1.3}
  .contacts{margin-top:18px;font-size:14.5px;line-height:1.45;list-style:none}
  .contacts li{display:flex;justify-content:flex-end;align-items:center;gap:8px}
  .contacts svg{width:11px;height:11px;fill:var(--orange)}
  .contacts .hl{color:var(--orange)}
  .ccb{position:absolute;left:40px;bottom:30px;color:var(--white);font-size:15px;letter-spacing:.5px}
</style>
</head>
<body>
  <section class="card card-front">
    <div class="brand-front">
      <span class="brand-mark"></span>
      <span class="brand-name">HomeWise</span>
    </div>
    <p class="services">Occupational Therapy<span class="dot"></span>Home safety &amp; accessibility assessments<br>Home modification consulting<span class="dot"></span>Project management</p>
    <p class="site-front">www.<b>homewiseforyears</b>.com</p>
  </section>

  <section class="card card-back">
    <svg class="swoop" viewBox="0 0 660 377" preserveAspectRatio="none">
      <path d="M22,0 H660 V292 L470,296 C240,300 40,240 22,0 Z" fill="var(--grey)"/>
      <path d="M44,0 H660 V292 L470,292 C260,296 62,236 44,0 Z" fill="var(--white)"/>
    </svg>
    <div class="brand-back">
      <span class="brand-mark"></span>
      <span class="brand-name">HomeWise</span>
    </div>
    <div class="details">
      <p class="person">Danielle Reyes Crawford</p>
      <p class="role">OTR/L, CAPS, ECHM, Occupational Therapist<br>Home Modification &amp; Accessibility Specialist.</p>
      <ul class="contacts">
        <li>(503) 218-4057 <svg viewBox="0 0 24 24"><path d="M6.6 10.8a15 15 0 0 0 6.6 6.6l2.2-2.2c.3-.3.7-.4 1-.2 1.1.4 2.3.6 3.6.6.6 0 1 .4 1 1V20c0 .6-.4 1-1 1A17 17 0 0 1 3 4c0-.6.4-1 1-1h3.5c.6 0 1 .4 1 1 0 1.3.2 2.5.6 3.6.1.3 0 .7-.2 1z"/></svg></li>
        <li>homewiseforyears@nestmail.example <svg viewBox="0 0 24 24"><path d="M2 5h20v14H2zm2 2v.5l8 5 8-5V7l-8 5z"/></svg></li>
        <li>www.<span class="hl">homewiseforyears</span>.com <svg viewBox="0 0 24 24"><circle cx="12" cy="12" r="10"/></svg></li>
      </ul>
    </div>
    <p class="ccb">CCB #: 487315</p>
  </section>
</body>
</html>
```